KRT Flyer - Workshop and Scholarship Program

KRT needs a double sided flyer designed for an upcoming workshop we have that is also doubling as a launch of our business and of our scholarship program.
All of the information required to go onto the flyer is contained below in the two documents.
The first is a word document that contains the details to be included on the flyer - this is in the order that I wish to present them also.
The second document is an earlier example of a winning flyer that was designed for an earlier launch. I was happy with many of the characteristics within this flyer including the photo/bio at the bottom.
Please note that the language and descriptions have all changed.
Please use images and patterns that you feel address the requirements of the advertisement.
I have included the original design files for the logo and flyer to get the logo and bio image
Target Market(s)
HSC students (Final Year of High School
Industry/Entity Type
Education
Font styles to use
Other font styles liked:
- Myriad Pro
Requirements
Must have
- The logo of the business must be shown a maximum of twice on both sides. Please remove the surrounding square and imbed it into the flyer.
- A simple but effective design
Nice to have
- Images that reflect the content
Should not have
- Too much going on that the message is lost.

```html
<!DOCTYPE html>
<html lang="en">
<head>
<meta charset="utf-8">
<title>KRT Flyer – HSC Preparation Workshop</title>
<link rel="stylesheet" href="https://fonts.googleapis.com/css2?family=Open+Sans:wght@600;700;800&family=Source+Sans+3:wght@400;600;700&display=swap">
<style>
  :root {
    --navy: #1c2a3d;
    --orange: #f36f21;
    --white: #ffffff;
    --ink: #2a3140;
    --page-bg: #e9e7e3;
    --photo-a: #d9d3cb;
    --photo-b: #8f7a6a;
    --photo-c: #4d6b8a;
  }
  * { box-sizing: border-box; margin: 0; padding: 0; }
  html, body { width: 1200px; height: 1200px; overflow: hidden; }
  body {
    background: var(--page-bg);
    font-family: "Source Sans 3", "Helvetica Neue", Arial, sans-serif;
    color: var(--ink);
  }
  .flyer {
    position: absolute;
    left: 242px; top: 96px;
    width: 715px; height: 1008px;
    background: var(--white);
    overflow: hidden;
    box-shadow: 0 6px 18px rgba(0,0,0,.18);
  }
  .layer { position: absolute; left: 0; top: 0; width: 715px; height: 600px; }

  .brand {
    position: absolute; left: 40px; top: 42px;
    display: flex; align-items: center; gap: 10px;
  }
  .brand-dot { width: 22px; height: 22px; border-radius: 50%; background: var(--orange); }
  .brand-name {
    font-family: "Open Sans", Arial, sans-serif;
    font-weight: 800; font-size: 44px; letter-spacing: 1px;
    color: var(--navy); line-height: 1;
  }

  .banner {
    position: absolute; left: 0;
    color: var(--white);
    font-family: "Open Sans", Arial, sans-serif;
    font-weight: 700; font-size: 12.5px;
    white-space: nowrap;
    display: flex; align-items: center;
    padding-left: 26px;
  }
  .banner--spots {
    top: 440px; height: 30px; width: 420px; background: var(--navy);
    clip-path: polygon(0 0, 100% 0, 96% 100%, 0 100%);
  }
  .banner--event {
    top: 482px; height: 30px; width: 460px; background: var(--orange);
    clip-path: polygon(0 0, 100% 0, 96% 100%, 0 100%);
  }

  .headline {
    position: absolute; left: 0; top: 590px; width: 715px;
    text-align: center;
    font-family: "Open Sans", Arial, sans-serif;
    font-weight: 700; font-size: 28px; line-height: 40px;
    color: var(--navy);
  }
  .headline .accent { color: var(--orange); }

  .section-title {
    position: absolute; left: 18px; top: 672px;
    font-family: "Open Sans", Arial, sans-serif;
    font-weight: 700; font-size: 17px; line-height: 22px; color: var(--orange);
  }

  .agenda {
    position: absolute; left: 0; top: 0; list-style: none;
    font-size: 12.5px; line-height: 16px; color: var(--ink);
  }
  .agenda > li { position: absolute; padding-left: 22px; }
  .agenda--left > li { left: 18px; width: 352px; }
  .agenda--left > li:nth-child(1) { top: 714px; }
  .agenda--left > li:nth-child(2) { top: 744px; }
  .agenda--left > li:nth-child(3) { top: 772px; width: 300px; }
  .agenda--left > li:nth-child(4) { top: 810px; width: 300px; }
  .agenda--left > li:nth-child(5) { top: 848px; }
  .agenda--left > li:nth-child(6) { top: 874px; letter-spacing: -0.1px; }
  .agenda--right > li { left: 386px; top: 700px; width: 320px; padding-left: 26px; }
  .tick { position: absolute; left: 0; top: 1px; width: 14px; height: 13px; }

  .methods { list-style: none; margin-top: 16px; }
  .methods li {
    margin-bottom: 5px; line-height: 16px;
    font-weight: 700; font-size: 13px; color: var(--orange);
  }

  .call-stripe {
    position: absolute; left: 366px; top: 824px;
    width: 349px; height: 94px; background: var(--orange);
    clip-path: polygon(3% 0, 100% 0, 100% 100%, 0 100%);
  }
  .call-box {
    position: absolute; left: 376px; top: 824px;
    width: 339px; height: 94px;
    background: var(--navy);
    clip-path: polygon(4% 0, 100% 0, 100% 100%, 0 100%);
    text-align: center; padding-top: 6px; padding-left: 8px;
  }
  .call-label {
    font-family: "Open Sans", Arial, sans-serif;
    font-weight: 700; font-size: 30px; color: var(--orange); line-height: 40px;
  }
  .call-number {
    font-family: "Open Sans", Arial, sans-serif;
    font-weight: 700; font-size: 34px; color: var(--white); line-height: 42px;
  }

  .register {
    position: absolute; left: 0; top: 918px; width: 715px; height: 90px;
    background: var(--navy); color: var(--white);
    padding: 10px 20px 0 20px;
  }
  .register-title {
    font-family: "Open Sans", Arial, sans-serif;
    font-weight: 700; font-size: 19px; line-height: 26px; color: var(--orange); margin-bottom: 6px;
  }
  .register-text { font-size: 13px; line-height: 18px; }
</style>
</head>
<body>
  <main class="flyer">
    <svg class="layer photo" viewBox="0 0 715 600" role="img" aria-label="Photo of smiling senior students giving thumbs up, one in a graduation cap holding a diploma">
      <defs>
        <linearGradient id="photoTone" x1="0" y1="0" x2="1" y2="1">
          <stop offset="0" stop-color="var(--photo-a)"/>
          <stop offset="0.55" stop-color="var(--photo-b)"/>
          <stop offset="1" stop-color="var(--photo-c)"/>
        </linearGradient>
      </defs>
      <path d="M0,184 C230,184 480,128 715,36 L715,442 C500,520 260,568 0,570 Z" fill="url(#photoTone)"/>
    </svg>

    <svg class="layer swooshes" viewBox="0 0 715 600" aria-hidden="true">
      <path class="swoosh-top-orange" d="M0,130 L0,146 C150,146 300,132 402,112 C300,124 150,132 0,130 Z" fill="var(--orange)"/>
      <path class="swoosh-top-navy" d="M0,158 C230,160 480,110 715,26 L715,38 C480,130 230,186 0,186 Z" fill="var(--navy)"/>
      <path class="swoosh-bottom-orange" d="M336,524 C480,500 620,460 715,412 L715,432 C620,478 480,512 336,524 Z" fill="var(--orange)"/>
      <path class="swoosh-bottom-navy" d="M0,564 C250,562 500,510 715,440 L715,458 C500,530 250,586 0,588 Z" fill="var(--navy)"/>
    </svg>

    <div class="brand">
      <span class="brand-dot"></span>
      <span class="brand-name">KRT</span>
    </div>

    <div class="banner banner--spots">Limited spots available at both venues! Don’t miss out!</div>
    <div class="banner banner--event">This event could make all the difference to your HSC Experience!</div>

    <h1 class="headline">2017 <span class="accent">FREE HSC PREPARATION WORKSHOP</span><br>AND SCHOLARSHIP OFFER</h1>

    <h2 class="section-title">What will the day involve?</h2>

    <ul class="agenda agenda--left">
      <li><svg class="tick" viewBox="0 0 15 14"><path d="M1,7 L5.5,12 L14,1" fill="none" stroke="var(--orange)" stroke-width="2.6"/></svg>Establishing individual goals for the year ahead</li>
      <li><svg class="tick" viewBox="0 0 15 14"><path d="M1,7 L5.5,12 L14,1" fill="none" stroke="var(--orange)" stroke-width="2.6"/></svg>Developing the right mindset for the HSC</li>
      <li><svg class="tick" viewBox="0 0 15 14"><path d="M1,7 L5.5,12 L14,1" fill="none" stroke="var(--orange)" stroke-width="2.6"/></svg>Participating in case studies that simulate the Year 12 experience</li>
      <li><svg class="tick" viewBox="0 0 15 14"><path d="M1,7 L5.5,12 L14,1" fill="none" stroke="var(--orange)" stroke-width="2.6"/></svg>Understanding the importance of starting early and keeping up to date</li>
      <li><svg class="tick" viewBox="0 0 15 14"><path d="M1,7 L5.5,12 L14,1" fill="none" stroke="var(--orange)" stroke-width="2.6"/></svg>Learning about the importance of maintaining notes</li>
      <li><svg class="tick" viewBox="0 0 15 14"><path d="M1,7 L5.5,12 L14,1" fill="none" stroke="var(--orange)" stroke-width="2.6"/></svg>Strategies to increase the EFFICIENCY AND EFFECTIVENESS<br>of your studies while decreasing levels of PROCRASTINATION</li>
    </ul>

    <ul class="agenda agenda--right">
      <li><svg class="tick" viewBox="0 0 15 14"><path d="M1,7 L5.5,12 L14,1" fill="none" stroke="var(--orange)" stroke-width="2.6"/></svg>Planning a BALANCED approach to studies and<br>AVOIDING BURNOUT with:
        <ul class="methods">
          <li>The 4 stages of examination preparation</li>
          <li>The 7 habits of highly effective students</li>
          <li>The 8 steps to Academic Success</li>
        </ul>
      </li>
    </ul>

    <div class="call-stripe"></div>
    <div class="call-box">
      <div class="call-label">CALL US NOW</div>
      <div class="call-number">555 -014-203</div>
    </div>

    <section class="register">
      <h3 class="register-title">How to register:</h3>
      <p class="register-text">Text 0400 555 019 with your name, email address and the session date and time you wish to attend.<br>An email will then be sent confirming further details.</p>
    </section>
  </main>
</body>
</html>
```